LWTrendco

I ran out of business cards I designed myself on line. THe company went out of business and I LOVE my card. I am hoping someone can recreate the look or something equally as appealing to me.

Industry/Entity Type

Business

Colors
ecdaeb
f7f1f7

Requirements
Must have
• The card is going to be printed by a company Quibzo.com. they are very high end stock and I market to high end clients…the logo needs to remain small and centered at the top. If it helps my web site is lwtrendco.net you can see there how I left the logo very small

```html
<!DOCTYPE html>
<html lang="en">
<head>
<meta charset="utf-8">
<title>LW Trendco, LLC — Business Card</title>
<link rel="stylesheet" href="https://fonts.googleapis.com/css2?family=Cinzel:wght@400;600&display=swap">
<style>
  :root {
    --page: #ffffff;
    --card-border: #ecdaeb;
    --card-face: #f7f1f7;
    --mark-tint: #ecdaeb;
    --brand-ink: #3b3232;
    --ink: #141414;
  }
  html, body {
    margin: 0;
    padding: 0;
    width: 1200px;
    height: 1000px;
    overflow: hidden;
    background: var(--page);
  }
  .canvas {
    position: relative;
    width: 1200px;
    height: 1000px;
  }
  .card {
    position: absolute;
    left: 226px;
    top: 0;
    width: 670px;
    height: 1000px;
    background: var(--card-border);
  }
  .card-face {
    position: absolute;
    left: 48px;
    top: 48px;
    width: 573px;
    height: 902px;
    background: var(--card-face);
    font-family: "Cinzel", Georgia, serif;
    color: var(--ink);
    text-align: center;
  }
  .brand-mark {
    position: absolute;
    left: 50%;
    top: 90px;
    width: 150px;
    height: 150px;
    margin-left: -75px;
    background: var(--mark-tint);
  }
  .brand-name {
    position: absolute;
    left: 0;
    right: 0;
    top: 308px;
    margin: 0;
    font-size: 38px;
    font-weight: 400;
    letter-spacing: 2px;
    color: var(--brand-ink);
  }
  .services {
    position: absolute;
    left: 0;
    right: 0;
    top: 486px;
    margin: 0;
    font-size: 33px;
    font-weight: 600;
    letter-spacing: 0.5px;
  }
  .contact {
    position: absolute;
    left: 0;
    right: 0;
    top: 680px;
    margin: 0;
    font-style: normal;
    font-size: 33px;
    font-weight: 600;
    line-height: 57px;
  }
  .contact span { display: block; }
  .contact .phone { font-weight: 400; }
</style>
</head>
<body>
  <main class="canvas">
    <section class="card">
      <div class="card-face">
        <div class="brand-mark" aria-hidden="true"></div>
        <h1 class="brand-name">LW Trendco, LLC</h1>
        <p class="services">Design &amp; Renovation</p>
        <address class="contact">
          <span class="person">Marielle Dovane</span>
          <span class="phone">420-555-0187</span>
          <span class="email">marielle@lwtrendco.net</span>
        </address>
      </div>
    </section>
  </main>
</body>
</html>
```